Banner Ad Design Project

Hello,

I need 2 banner designs for advertising on zentrix pubmark. Each design must be declined in the following format :

- 300 x 50 Leaderboard pour mobiles
- 468 x 60 Bannière
- 728 x 90 Leaderboard
- 250 x 250 Carré
- 200 x 200 Petit carré
- 336 x 280 Grand rectangle
- 300 x 250 Rectangle intégré
- 120 x 600 Skyscraper
- 160 x 600 Skyscraper large

The banners are to promote an "home exchange" site : http://www.brindlevaxo.net

Here are the 2 texts that must appear on the banners:
- Say "bye bye" to hotel bill! Stay for free with Brindlevaxo!
- Travel worldwide for free with Brindlevaxo!

Target Market(s)

English customer world wide

Industry/Entity Type

Advertising

Requirements
Must have
• The name "Brindlevaxo" must appear on each banner
The banner must have a look and feel similar of the website http://www.brindlevaxo.net

```html
<!DOCTYPE html>
<html lang="en">
<head>
<meta charset="utf-8">
<title>Brindlevaxo banner set</title>
<link rel="stylesheet" href="https://fonts.googleapis.com/css2?family=Arimo:wght@500;700&display=swap">
<style>
  :root {
    --navy: #1a3680;
    --mid-blue: #5a8cc6;
    --sky: #a9c7e4;
    --mist: #f2f6fa;
    --white: #ffffff;
    --green: #76bd1d;
    --green-edge: #ffffff;
    --case-blue: #2a74e0;
    --case-green: #7cc11a;
    --frame: #dde3ea;
  }
  html, body {
    margin: 0;
    padding: 0;
    width: 1200px;
    height: 1154px;
    overflow: hidden;
    background: #ffffff;
    font-family: "Arimo", Arial, sans-serif;
  }
  .canvas { position: relative; width: 1200px; height: 1154px; }

  .banner {
    position: absolute;
    box-sizing: border-box;
    border: 1px solid var(--frame);
    overflow: hidden;
    color: var(--white);
  }
  .banner--rectangle {
    left: 28px; top: 28px; width: 521px; height: 435px;
    background: linear-gradient(180deg, var(--navy) 0%, var(--mid-blue) 45%, var(--sky) 70%, var(--mist) 100%);
  }
  .banner--skyscraper {
    left: 583px; top: 28px; width: 246px; height: 933px;
    background: linear-gradient(180deg, var(--navy) 0%, var(--mid-blue) 30%, var(--sky) 60%, var(--mist) 100%);
  }
  .banner--leaderboard {
    left: 28px; top: 978px; width: 1131px; height: 139px;
    background: linear-gradient(90deg, var(--navy) 0%, #2c56a0 30%, #7aa6d2 55%, #dfeaf4 80%, var(--mist) 100%);
  }

  .wordmark {
    position: absolute;
    margin: 0;
    font-weight: 500;
    color: var(--white);
    white-space: nowrap;
  }
  .banner--rectangle .wordmark { left: 28px; top: 12px; font-size: 56px; line-height: 72px; }
  .banner--skyscraper .wordmark { left: 23px; top: 18px; font-size: 56px; line-height: 59px; }
  .banner--leaderboard .wordmark { left: 24px; top: 8px; font-size: 48px; line-height: 56px; }

  .perks {
    position: absolute;
    margin: 0;
    padding: 0;
    list-style: none;
    font-weight: 700;
    white-space: nowrap;
  }
  .perks li { position: relative; padding-left: 27px; }
  .perks li::before {
    content: "";
    position: absolute;
    left: 4px;
    width: 8px; height: 8px;
    border-radius: 50%;
    background: var(--white);
  }
  .banner--rectangle .perks { left: 28px; top: 117px; font-size: 25px; line-height: 37px; }
  .banner--rectangle .perks li + li { margin-top: 14px; }
  .banner--rectangle .perks li::before { top: 15px; }

  .banner--skyscraper .perks { left: 18px; top: 237px; font-size: 25px; line-height: 37px; }
  .banner--skyscraper .perks li + li { margin-top: 14px; }
  .banner--skyscraper .perks li::before { top: 15px; }

  .banner--leaderboard .perks { left: 31px; top: 69px; font-size: 22px; line-height: 34px; }
  .banner--leaderboard .perks li::before { top: 13px; width: 7px; height: 7px; }

  .luggage {
    position: absolute;
    border-radius: 14px;
    background: linear-gradient(100deg, var(--case-blue) 0%, var(--case-blue) 55%, var(--case-green) 60%, var(--case-green) 100%);
  }
  .banner--rectangle .luggage { left: 303px; top: 191px; width: 203px; height: 226px; }
  .banner--skyscraper .luggage { left: 26px; top: 558px; width: 203px; height: 229px; }
  .banner--leaderboard .luggage { left: 678px; top: 9px; width: 200px; height: 130px; border-radius: 14px 14px 0 0; }

  .cta {
    position: absolute;
    box-sizing: border-box;
    display: flex;
    align-items: center;
    justify-content: center;
    background: var(--green);
    border: 3px solid var(--green-edge);
    border-radius: 10px;
    color: var(--white);
    font-weight: 700;
    font-size: 26px;
    text-decoration: none;
    box-shadow: 0 1px 3px rgba(0,0,0,0.15);
  }
  .banner--rectangle .cta { left: 40px; top: 334px; width: 233px; height: 64px; }
  .banner--skyscraper .cta { left: 9px; top: 822px; width: 233px; height: 64px; }
  .banner--leaderboard .cta { left: 881px; top: 44px; width: 232px; height: 59px; }
</style>
</head>
<body>
<main class="canvas">

  <section class="banner banner--rectangle" aria-label="Brindlevaxo 336 by 280 rectangle">
    <h2 class="wordmark">Brindlevaxo</h2>
    <ul class="perks">
      <li>Say "bye bye" to hotel<br>bill! Stay for free</li>
      <li>Travel worldwide<br>for free</li>
    </ul>
    <div class="luggage" role="img" aria-label="Illustration of a blue and a green suitcase"></div>
    <a class="cta" href="http://www.brindlevaxo.net">Post my home</a>
  </section>

  <section class="banner banner--skyscraper" aria-label="Brindlevaxo 160 by 600 wide skyscraper">
    <h2 class="wordmark">Brindle<br>vaxo</h2>
    <ul class="perks">
      <li>Say "bye bye"<br>to hotel bill!<br>Stay for free</li>
      <li>Travel<br>worldwide<br>for free</li>
    </ul>
    <div class="luggage" role="img" aria-label="Illustration of a blue and a green suitcase"></div>
    <a class="cta" href="http://www.brindlevaxo.net">Post my home</a>
  </section>

  <section class="banner banner--leaderboard" aria-label="Brindlevaxo 728 by 90 leaderboard">
    <h2 class="wordmark">Brindlevaxo</h2>
    <ul class="perks">
      <li>Say "bye bye" to hotel bill! Stay for free</li>
      <li>Travel worldwide for free</li>
    </ul>
    <div class="luggage" role="img" aria-label="Illustration of a blue and a green suitcase"></div>
    <a class="cta" href="http://www.brindlevaxo.net">Post my home</a>
  </section>

</main>
</body>
</html>
```